Need a graphic design to promote our new online learning system

We are seeking a graphic design to be promoted on social media to promote our new Online earning Management system (OKRU-LMS). The purpose is to make the design attractive and informative for parents and students so they can enrol at our School.

It must state the benefits of the OKRU-LMS. Colourful but not too busy.

```html
<!DOCTYPE html>
<html lang="en">
<head>
<meta charset="UTF-8">
<title>Kestrel Ridge Academy – Enrol at Our School with OKRU-LMS</title>
<link rel="stylesheet" href="https://fonts.googleapis.com/css2?family=Cinzel:wght@500&family=Montserrat:wght@800;900&display=swap">
<style>
  :root {
    --sky-blue: #0a86c9;
    --deep-blue: #0b4c9c;
    --mid-blue: #0d5fb0;
    --accent-cyan: #0aa3e8;
    --white: #ffffff;
    --photo-light: #e9e4da;
    --photo-mid: #b49374;
    --photo-dark: #5a4a3e;
  }
  * { margin: 0; padding: 0; box-sizing: border-box; }
  html, body { width: 675px; height: 1200px; overflow: hidden; }
  body { font-family: "Montserrat", Arial, sans-serif; color: var(--white); }

  .poster {
    position: relative;
    width: 675px;
    height: 1200px;
    overflow: hidden;
    background: linear-gradient(180deg, var(--sky-blue) 0%, var(--mid-blue) 45%, var(--deep-blue) 100%);
  }

  .campus-backdrop {
    position: absolute;
    inset: 0;
    background:
      radial-gradient(ellipse 70% 40% at 85% 25%, rgba(20, 70, 150, 0.55), transparent 70%),
      radial-gradient(ellipse 40% 35% at 15% 45%, rgba(15, 80, 160, 0.45), transparent 70%),
      linear-gradient(160deg, rgba(255,255,255,0.04) 0%, rgba(0,30,90,0.25) 100%);
  }

  .brand-mark {
    position: absolute;
    top: 64px;
    left: 290px;
    width: 94px;
    height: 94px;
    background: var(--white);
  }
  .brand-name {
    position: absolute;
    left: 0;
    width: 100%;
    text-align: center;
    font-family: "Cinzel", "Times New Roman", serif;
    font-weight: 500;
    line-height: 1;
    color: var(--white);
  }
  .brand-name-main {
    top: 180px;
    font-size: 56px;
    letter-spacing: 8px;
    padding-left: 8px;
  }
  .brand-name-sub {
    top: 257px;
    font-size: 25px;
    letter-spacing: 2px;
  }
  .brand-name-sub span {
    display: inline-block;
    padding: 0 4px 8px;
    border-bottom: 3px solid var(--white);
  }

  .headline {
    position: absolute;
    inset: 0;
    font-weight: 900;
    text-transform: uppercase;
    line-height: 1;
  }
  .headline span {
    position: absolute;
    left: 0;
    width: 100%;
    text-align: center;
    transform-origin: center;
  }
  .headline-top {
    top: 340px;
    font-size: 70px;
    transform: scaleX(0.935);
  }
  .headline-main {
    top: 396px;
    font-size: 135px;
    letter-spacing: -3px;
    transform: scaleX(0.925);
  }

  .exam-photo {
    position: absolute;
    left: 78px;
    top: 559px;
    width: 530px;
    height: 275px;
    background: linear-gradient(100deg, var(--photo-light) 0%, #c9b9a4 35%, var(--photo-mid) 60%, var(--photo-dark) 100%);
  }

  .section-tag {
    position: absolute;
    left: 78px;
    top: 863px;
    width: 462px;
    height: 60px;
  }
  .section-tag svg { position: absolute; inset: 0; }
  .section-tag-label {
    position: absolute;
    left: 27px;
    top: 0;
    line-height: 60px;
    font-size: 50px;
    font-weight: 900;
    letter-spacing: 0.5px;
  }

  .body-copy {
    position: absolute;
    left: 81px;
    top: 942px;
    font-size: 21px;
    font-weight: 800;
    line-height: 28.7px;
    text-transform: uppercase;
    letter-spacing: 0.3px;
  }
  .body-copy .line { display: block; white-space: nowrap; }
  .body-copy .highlight { color: var(--accent-cyan); }
</style>
</head>
<body>
  <main class="poster">
    <div class="campus-backdrop" role="img" aria-label="Modern school campus building in blue tones"></div>

    <span class="brand-mark" aria-hidden="true"></span>
    <div class="brand-name brand-name-main">Kestrel Ridge</div>
    <div class="brand-name brand-name-sub"><span>ACADEMY OF LEARNING</span></div>

    <h1 class="headline">
      <span class="headline-top">Enrol at our</span>
      <span class="headline-main">School</span>
    </h1>

    <div class="exam-photo" role="img" aria-label="Students writing at wooden desks in an exam hall"></div>

    <div class="section-tag">
      <svg width="462" height="60" viewBox="0 0 462 60" aria-hidden="true">
        <polygon points="0,0 409,0 462,60 0,60" fill="var(--accent-cyan)"/>
      </svg>
      <h2 class="section-tag-label">OKRU-LMS</h2>
    </div>

    <p class="body-copy">
      <span class="line">Learn anytime, anywhere with our</span>
      <span class="line">new OKRU-LMS online learning system.</span>
      <span class="line">Access lessons, submit assignments</span>
      <span class="line">and track grades in one place while</span>
      <span class="line">parents follow progress live. <span class="highlight">Enrol</span></span>
      <span class="line highlight">today and start learning</span>
      <span class="line highlight">smarter with OKRU-LMS.</span>
    </p>
  </main>
</body>
</html>
```